Card Design for my dog training business Rustpaw Obedience

Need a business card design for my dog training business with my new logo. Want the card to come off professional yet fun. Want it to be very eye catchy as well. I normally have these at vet clinics, pet stores, and groomers. so need it to look better than my competitors.
Target Market(s)
dog owners
Industry/Entity Type
Dog Training
Contact Information for Business Card
needs logo, my name and info
Font styles to use
Serif
Colors
0255a3
ffffff
ec1f27
000000
333333
fbfbfb
Requirements
Must have
- Rustpaw Obedience
- Hollis Brandt
- 415 903 2267
- info@rustpawobedience.example
- www.rustpawobedience.example

```html
<!DOCTYPE html>
<html lang="en">
<head>
<meta charset="utf-8">
<title>Rustpaw Obedience – Business Card</title>
<link href="https://fonts.googleapis.com/css2?family=Libre+Baskerville:ital,wght@0,400;0,700;1,400&display=swap" rel="stylesheet">
<style>
  :root {
    --backdrop: #cfe9df;
    --card-black: #231f20;
    --band-white: #ffffff;
    --ink: #333333;
    --silver: #c9c9c9;
    --icon-grey: #5a5a5a;
    --card-w: 490px;
    --card-h: 280px;
  }
  * { box-sizing: border-box; margin: 0; padding: 0; }
  html, body {
    width: 1200px; height: 856px; overflow: hidden;
    background: var(--backdrop);
    font-family: "Libre Baskerville", "Times New Roman", serif;
  }
  .sheet {
    width: 1200px; height: 856px;
    display: flex; align-items: center; justify-content: center; gap: 60px;
  }
  .card {
    position: relative;
    width: var(--card-w); height: var(--card-h);
    border-radius: 30px;
    background: var(--card-black);
    overflow: hidden;
    box-shadow: 0 10px 24px rgba(0,0,0,.18);
  }
  /* Front */
  .card-front .info-band {
    position: absolute; left: 0; right: 0; top: 128px; height: 112px;
    background: var(--band-white);
  }
  .card-front .brand {
    position: absolute; top: 42px; left: 0; right: 0;
    display: flex; align-items: center; justify-content: center; gap: 10px;
    color: var(--silver); font-size: 20px; font-weight: 700; letter-spacing: .5px;
  }
  .brand-dot {
    width: 12px; height: 12px; border-radius: 50%; background: var(--silver);
  }
  .holder-name {
    position: absolute; left: 36px; top: 208px;
    font-size: 15px; font-weight: 700; color: var(--ink); letter-spacing: .6px;
    text-transform: uppercase;
  }
  .contact-list {
    position: absolute; left: 262px; top: 140px;
    list-style: none;
  }
  .contact-list li {
    display: flex; align-items: center; gap: 8px;
    font-size: 10.5px; font-weight: 700; color: var(--ink);
    height: 19px;
  }
  .contact-icon { width: 11px; height: 11px; flex: none; }
  /* Back */
  .card-back {
    display: flex; flex-direction: column; align-items: center; justify-content: center;
  }
  .card-back .brand {
    display: flex; align-items: center; gap: 12px;
    color: #ffffff; font-size: 24px; font-weight: 700; letter-spacing: .5px;
  }
  .card-back .brand-dot { background: #ffffff; width: 14px; height: 14px; }
  .tagline {
    margin-top: 14px;
    color: #ffffff; font-size: 9px; font-style: italic; letter-spacing: .3px;
  }
</style>
</head>
<body>
  <main class="sheet">
    <section class="card card-front" aria-label="Business card front">
      <div class="brand"><span class="brand-dot"></span>Rustpaw Obedience</div>
      <div class="info-band"></div>
      <p class="holder-name">Hollis Brandt</p>
      <ul class="contact-list">
        <li>
          <svg class="contact-icon" viewBox="0 0 12 12" aria-hidden="true">
            <circle cx="6" cy="6" r="6" fill="var(--icon-grey)"/>
            <path d="M4 3.2l1 1.1-.5.8c.4.9 1 1.5 1.9 1.9l.8-.5 1.1 1-.6 1c-2.3-.2-4.4-2.3-4.6-4.6z" fill="#fff"/>
          </svg>415 903 2267
        </li>
        <li>
          <svg class="contact-icon" viewBox="0 0 12 12" aria-hidden="true">
            <circle cx="6" cy="6" r="6" fill="var(--icon-grey)"/>
            <rect x="3" y="4" width="6" height="4.2" fill="none" stroke="#fff" stroke-width=".8"/>
            <path d="M3 4l3 2.3L9 4" fill="none" stroke="#fff" stroke-width=".8"/>
          </svg>info@rustpawobedience.example
        </li>
        <li>
          <svg class="contact-icon" viewBox="0 0 12 12" aria-hidden="true">
            <circle cx="6" cy="6" r="6" fill="var(--icon-grey)"/>
            <circle cx="6" cy="6" r="3" fill="none" stroke="#fff" stroke-width=".7"/>
            <path d="M3 6h6M6 3c-1.4 1.6-1.4 4.4 0 6M6 3c1.4 1.6 1.4 4.4 0 6" fill="none" stroke="#fff" stroke-width=".6"/>
          </svg>www.rustpawobedience.example
        </li>
      </ul>
    </section>

    <section class="card card-back" aria-label="Business card back">
      <div class="brand"><span class="brand-dot"></span>Rustpaw Obedience</div>
      <p class="tagline">“Good manners start here, one walk at a time.”</p>
    </section>
  </main>
</body>
</html>
```